Medical centre needs a business card

We are a medcial centre in Australia, needing a new business card. Our demographic is low working class families. We are going to be renovating our premises to modernise the look and also had a new logo done a few months ago representing quality and community, and now need to update our cards. It needs to be doubled sided, with logo and contact details on the front, and appointment details on the back. . Needs to be modern and simple, easy to read. <br/><br/>Name: Fern Vale Medical Centre <br/>Address: 512 Kestrel Rd (Cnr Kestrel Rd & Lindon Park Rd),<br/>Corvane Court Shopping Centre, Paralowie, SA 5108<br/>Ph: 08 8361 4027<br/>Tag line: Where every visit counts for you<br/>Website: www.fernvalemedicalcentre.example.au<br/>Online bookings also available<br/><br/>(On the back, to have 3 lines of appointments that can be written in.<br/>Day, date, time)<br/><br/>Your next appointment is on<br/>Can try “M T W Th F Sa Su _________________ at ____________ am/pm” or other combinations <br/>Please advise as soon as possible if unable to attend<br/>Cancellation fees apply if less than 2 hrs notice<br/>Online appointments available (please highlight this option by either by position, colour or font)

Target Market(s)

Lower social economic working class, young families to seniors

Industry/Entity Type

Medical Centre

Contact Information for Business Card

Fern Vale Medical Centre
512 Kestrel Rd (Cnr Kestrel Rd & Lindon Park Drive)
Corvane Court Shopping Centre
Marrowby SA 5097
Ph: 08 8361 4027
www.fernvalemedicalcentre.example.au
Tagline line: where every visit counts for you
Back side is for appointments
Your next appointment is with Dr ______________
Day/date/time (Please give 3 lines of appointments)
Please advise as soon as possible if unable to attend
Cancellation fees apply if less than 2 hours notice
Online appointments available
Book online easily and conveniently (please highlight online appointments)

Font styles to use
Serif
Sans Serif

Colors

Designer to choose colors to be used in the design.

Requirements
Must have
• Modern and simple
• Easy to ready
• Induces a wellbeing feeling
• Incorporate our logo colours and feel from logo
• Induces feeling of stability and security
Nice to have
• Attract attention
• Pleasant to look at
• Feeling of innovation
Should not have
• Loud clashing colours
• Overly luxurious feeling
• Overly artistic

```html
<!DOCTYPE html>
<html lang="en">
<head>
<meta charset="utf-8">
<title>Fern Vale Medical Centre – Business Card</title>
<link rel="stylesheet" href="https://fonts.googleapis.com/css2?family=Open+Sans:ital,wght@0,400;0,600;0,700;1,600&display=swap">
<style>
  :root {
    --blue: #0b72bb;
    --blue-dark: #075c9a;
    --green: #a5cf4c;
    --green-bright: #b4db3a;
    --ink: #1d1d1d;
    --paper: #ffffff;
    --backdrop: #e9ecef;
  }
  * { box-sizing: border-box; margin: 0; padding: 0; }
  html, body {
    width: 1200px; height: 1021px; overflow: hidden;
    background: var(--backdrop);
    font-family: "Open Sans", sans-serif;
    color: var(--ink);
  }
  .canvas { position: relative; width: 1200px; height: 1021px; }

  .card {
    position: absolute; left: 240px; width: 720px; height: 410px;
    overflow: hidden; box-shadow: 0 6px 20px rgba(0,0,0,.18);
  }

  /* ---------- Appointment side ---------- */
  .card-back { top: 45px; background: var(--green); }
  .appointment-tab {
    position: absolute; top: 24px; left: 340px; width: 350px; height: 52px;
    background: var(--blue); border-radius: 10px;
    color: var(--paper); font-weight: 700; font-size: 19px; letter-spacing: .5px;
    display: flex; align-items: center; justify-content: center;
  }
  .field { position: absolute; font-size: 16px; display: flex; align-items: flex-end; }
  .field .line { display: block; border-bottom: 1.5px solid var(--paper); height: 18px; margin: 0 8px; }
  .field-doctor { top: 66px; left: 40px; }
  .field-doctor .line { width: 610px; }

  .days {
    position: absolute; top: 104px; left: 40px; width: 640px;
    display: flex; justify-content: space-between; font-size: 16px;
  }
  .day { display: flex; align-items: center; gap: 10px; }
  .day .box { width: 22px; height: 16px; background: var(--paper); }

  .slot { position: absolute; left: 40px; display: flex; align-items: flex-end; font-size: 16px; }
  .slot .line { display: block; border-bottom: 1.5px solid var(--paper); height: 18px; margin: 0 8px; }
  .slot .line-date { width: 300px; }
  .slot .line-time { width: 190px; }
  .slot-1 { top: 150px; }
  .slot-2 { top: 195px; }
  .slot-3 { top: 240px; }

  .notice {
    position: absolute; top: 282px; left: 0; width: 720px; text-align: center;
    font-size: 16px; line-height: 1.4;
  }
  .booking-band {
    position: absolute; left: 0; bottom: 0; width: 720px; height: 50px;
    background: var(--blue); color: var(--paper);
    display: flex; align-items: center; justify-content: center; gap: 8px;
    font-size: 16px;
  }
  .booking-band .highlight { color: var(--green-bright); font-weight: 700; font-style: italic; }

  /* ---------- Contact side ---------- */
  .card-front {
    top: 565px;
    background: linear-gradient(135deg, #ffffff 45%, #f1f5f7 100%);
  }
  .brand { position: absolute; top: 48px; left: 56px; display: flex; align-items: center; gap: 12px; }
  .brand .mark { width: 28px; height: 28px; background: var(--green); }
  .brand .name {
    font-weight: 700; font-size: 26px; line-height: 1.05; color: var(--blue);
    letter-spacing: .5px; text-transform: uppercase;
  }

  .contact { position: absolute; top: 140px; left: 56px; font-size: 17px; line-height: 1.32; }
  .contact .org { color: var(--blue); }
  .contact-row { display: flex; align-items: center; gap: 8px; }
  .contact-row svg { width: 16px; height: 16px; flex: none; }
  .contact-row.first { margin-top: 4px; }

  .person { position: absolute; top: 236px; right: 70px; text-align: right; }
  .person .full-name { color: var(--blue); font-weight: 700; font-size: 26px; }
  .person .role { font-size: 18px; }

  .tagline-band {
    position: absolute; left: 0; bottom: 0; width: 720px; height: 58px;
    background: var(--blue); border-top: 5px solid var(--green);
    color: var(--green-bright); font-weight: 600; font-size: 19px; letter-spacing: 3px;
    text-transform: uppercase;
    display: flex; align-items: center; justify-content: center;
  }
</style>
</head>
<body>
<main class="canvas">

  <section class="card card-back" aria-label="Appointment side">
    <div class="appointment-tab">YOUR NEXT APPOINTMENT</div>

    <div class="field field-doctor">Dr.:<span class="line"></span></div>

    <div class="days">
      <span class="day"><span class="box"></span>Mon</span>
      <span class="day"><span class="box"></span>Tue</span>
      <span class="day"><span class="box"></span>Wed</span>
      <span class="day"><span class="box"></span>Thu</span>
      <span class="day"><span class="box"></span>Fri</span>
      <span class="day"><span class="box"></span>Sat</span>
      <span class="day"><span class="box"></span>Sun</span>
    </div>

    <div class="slot slot-1">Date:<span class="line line-date"></span>Time:<span class="line line-time"></span>am/pm</div>
    <div class="slot slot-2">Date:<span class="line line-date"></span>Time:<span class="line line-time"></span>am/pm</div>
    <div class="slot slot-3">Date:<span class="line line-date"></span>Time:<span class="line line-time"></span>am/pm</div>

    <p class="notice">Please advise as soon as possible if unable to attend<br>Cancellation fees apply if less than 2 hours notice</p>

    <div class="booking-band">
      <span class="highlight">Online appointments available</span>
      <span>| Book online easily and conveniently</span>
    </div>
  </section>

  <section class="card card-front" aria-label="Contact side">
    <div class="brand">
      <span class="mark"></span>
      <span class="name">Fern Vale<br>Medical Centre</span>
    </div>

    <div class="contact">
      <div class="org">Fern Vale Medical Centre</div>
      <div>512 Kestrel Rd (Cnr Kestrel Rd &amp; Lindon Park Drive)</div>
      <div>Corvane Court Shopping Centre</div>
      <div>Marrowby SA 5097</div>
      <div class="contact-row first">
        <svg viewBox="0 0 16 16" aria-hidden="true"><path d="M4 1.5 6.2 4.6 4.9 6.2c.9 2 2.6 3.7 4.6 4.6l1.6-1.3 3.1 2.2-1.1 2.4C7.4 14.5 1.5 8.6 1.6 2.6Z" fill="#a5cf4c"/></svg>
        <span>08 8361 4027</span>
      </div>
      <div class="contact-row">
        <svg viewBox="0 0 16 16" aria-hidden="true"><g fill="none" stroke="#a5cf4c" stroke-width="1.4"><circle cx="8" cy="8" r="6.5"/><ellipse cx="8" cy="8" rx="2.8" ry="6.5"/><path d="M1.5 8h13"/></g></svg>
        <span>www.fernvalemedicalcentre.example.au</span>
      </div>
    </div>

    <div class="person">
      <div class="full-name">Daniel Ashford</div>
      <div class="role">Founder</div>
    </div>

    <div class="tagline-band">Where every visit counts for you</div>
  </section>

</main>
</body>
</html>
```